Up and coming Australian Systems Integrator needs a proposal template refresh

We need to update our proposal template and are looking for a fresh, modern, simple and elegant proposal template. We'd like to keep our existing logos if possible.
NovaLink is a privately owned company operating since 2006. Offices and technical staff located in Quarry Bay and Bendigo
Sustained, profitable growth year on year
Velnet strategic partner
Velnet Advanced Enterprise Network Architecture Specialisation
Velnet Advanced Security Architecture Specialisation
Velnet Advanced Collaboration Architecture Specialisation
Velnet Advanced Unified Computing Technology Specialisation
Velnet Advanced Data Centre Architecture Specialisation (in progress)
Velnet Gold Partner – Expect 2H2018
As well as being a Velnet partner we have a well established stable of other vendors such as Brakwell, Tavrimo, Harbourtone, DPQ, Moltrane Dialogic, Zell, SkyTrover, VoLERNA Drift)
We are a top two provider of Velnet product/services in the Victorian healthcare sector.
Updates
Please feel free to use different colors and fonts as we feel the existing ones look dated.

```html
<!DOCTYPE html>
<html lang="en">
<head>
<meta charset="utf-8">
<title>NovaLink Proposal Template</title>
<link rel="stylesheet" href="https://fonts.googleapis.com/css2?family=Montserrat:wght@400;600;700&family=Open+Sans:wght@400;600&display=swap">
<style>
:root{
  --navy:#1c2f5e;
  --blue:#2b579f;
  --sky:#4d86cf;
  --pale:#dfe8f4;
  --ink:#3a3f4a;
  --mute:#8a909c;
  --rule:#cfd5de;
  --stage:#e9ebef;
  --white:#ffffff;
}
*{margin:0;padding:0;box-sizing:border-box}
html,body{width:1200px;height:2184px;overflow:hidden;background:var(--stage)}
body{position:relative;font-family:"Open Sans",Arial,sans-serif;color:var(--ink)}
.spread{position:absolute;width:570px;height:412px;box-shadow:0 2px 8px rgba(20,30,60,.18)}
.col-a{left:20px}.col-b{left:610px}
.row-1{top:20px}.row-2{top:454px}.row-3{top:888px}.row-4{top:1322px}.row-5{top:1756px}
.page{position:absolute;top:0;width:285px;height:412px;background:var(--white);overflow:hidden}
.page.left{left:0}.page.right{left:285px;border-left:1px solid #eef0f3}
.logo{display:flex;align-items:center;gap:4px;font:700 8px "Montserrat",sans-serif;color:var(--navy);letter-spacing:.5px}
.logo i{display:block;width:7px;height:7px;background:var(--blue)}
.logo.light{color:var(--white)}.logo.light i{background:var(--white)}
.page-head{position:absolute;top:14px;right:18px}
.page-head-rule{position:absolute;top:28px;left:18px;right:18px;height:1px;background:var(--rule)}
.page-foot{position:absolute;bottom:12px;left:18px;right:18px;border-top:1px solid var(--rule);padding-top:3px;font-size:4.5px;color:var(--mute);display:flex;justify-content:space-between}
.title{position:absolute;left:18px;top:40px;font:700 12px "Montserrat",sans-serif;color:var(--blue)}
.title small{display:block;width:22px;height:2px;background:var(--blue);margin-top:4px}
.body{position:absolute;left:18px;right:18px;font-size:4.8px;line-height:1.55;color:var(--ink)}
.body p{margin-bottom:4px}
.sub{font:600 6px "Montserrat",sans-serif;color:var(--navy);margin:4px 0 3px}
.ph{background:linear-gradient(135deg,#5a7fae,#1f3560)}
.ph.light{background:linear-gradient(135deg,#c9d4e2,#7c8ea8)}
.ph.grey{background:linear-gradient(135deg,#d7dade,#9aa0a9)}
.abs{position:absolute}
.cols{display:grid;gap:10px}
.cols-2{grid-template-columns:1fr 1fr}.cols-3{grid-template-columns:1fr 1fr 1fr}
table{border-collapse:collapse;width:100%;font-size:4.5px}
td,th{border-bottom:1px solid var(--rule);padding:2px 3px;text-align:left}
th{background:var(--navy);color:var(--white);font-weight:600}
tr.hl td{background:var(--pale)}
.toc li{list-style:none;display:flex;font-size:5px;line-height:2;border-bottom:1px dotted var(--rule)}
.toc li span{flex:1}
.toc li.major{font-weight:600;color:var(--navy)}
.circle{border-radius:50%}
.cover-title{font:700 20px/1.1 "Montserrat",sans-serif;letter-spacing:.5px}
</style>
</head>
<body>

<section class="spread col-a row-1">
  <div class="page left" style="background:var(--navy)">
    <div class="abs ph" style="inset:0" role="img" aria-label="Blue-toned glass office tower rising into the sky"></div>
  </div>
  <div class="page right" style="background:linear-gradient(160deg,#2d5fae,#1a2d5a);border:none">
    <div class="abs" style="left:24px;top:40px"><div class="logo light"><i></i>NOVALINK</div></div>
    <div class="abs cover-title" style="left:24px;top:150px;color:var(--white)">DOCUMENT TITLE<br>DOLOR AMET</div>
    <div class="abs" style="left:24px;top:200px;font-size:6px;color:#c9d7ee">Proposal for Client Services Program</div>
    <div class="abs" style="left:24px;top:330px;font-size:5px;line-height:1.6;color:#c9d7ee">Prepared for: Client Name<br>Date: 01 Month 2018<br>Reference: NL-0001</div>
  </div>
</section>

<section class="spread col-b row-1">
  <div class="page left">
    <div class="abs" style="right:0;top:18px;width:40px;height:8px;background:var(--navy)"></div>
  </div>
  <div class="page right">
    <div class="abs" style="right:0;top:14px;width:50px;height:8px;background:var(--navy)"></div>
    <div class="page-head" style="top:30px"><div class="logo"><i></i>NOVALINK</div></div>
    <div class="abs ph" style="left:0;right:0;top:50px;height:150px" role="img" aria-label="Technician standing in a data centre server aisle"></div>
    <div class="abs cover-title" style="left:22px;top:220px;color:var(--navy);font-size:17px">DOCUMENT TITLE</div>
    <div class="abs" style="left:22px;top:242px;font-size:5.5px;color:var(--mute)">Proposal subtitle goes here</div>
    <svg class="abs" style="left:0;bottom:0" width="285" height="90" viewBox="0 0 285 90"><path d="M0 40 Q140 0 285 20 V90 H0Z" fill="var(--navy)"/><path d="M0 60 Q150 20 285 40 V90 H0Z" fill="var(--blue)"/></svg>
  </div>
</section>

<section class="spread col-a row-2">
  <div class="page left">
    <div class="page-head"><div class="logo"><i></i>NOVALINK</div></div>
    <div class="page-head-rule"></div>
    <div class="title">Document Control &amp; Confidentiality<small></small></div>
    <div class="body" style="top:70px">
      <div class="sub">Document Details</div>
      <table><tr><td>Title</td><td>Proposal Document</td></tr><tr><td>Client</td><td>Client Name</td></tr><tr><td>Author</td><td>Account Manager</td></tr></table>
      <div class="sub" style="margin-top:10px">Version Control</div>
      <table><tr><th>Version</th><th>Date</th><th>Author</th><th>Notes</th></tr><tr><td>0.1</td><td>01/05/18</td><td>Name</td><td>Draft</td></tr><tr><td>1.0</td><td>10/05/18</td><td>Name</td><td>Final</td></tr></table>
      <div class="sub" style="margin-top:10px">Distribution</div>
      <div style="height:8px;background:var(--sky);margin-bottom:4px"></div>
      <p>This document contains confidential information intended only for the named recipient.</p>
    </div>
    <div class="page-foot"><span>NovaLink Proposal</span><span>2</span></div>
  </div>
  <div class="page right">
    <div class="page-head"><div class="logo"><i></i>NOVALINK</div></div>
    <div class="page-head-rule"></div>
    <div class="title">Table of Contents<small></small></div>
    <ul class="body toc" style="top:70px">
      <li class="major"><span>1. Corporate Statement</span>3</li><li><span>1.1 Overview</span>4</li>
      <li class="major"><span>2. Executive Team</span>5</li><li><span>2.1 Our Service</span>6</li>
      <li class="major"><span>3. Solution Overview</span>7</li><li><span>3.1 Heading Template</span>8</li><li><span>3.2 Scope of Works</span>9</li>
      <li class="major"><span>4. Operational Reporting</span>10</li><li><span>4.1 Service Levels</span>11</li>
      <li class="major"><span>5. Options</span>12</li><li><span>5.1 Structure Chart</span>13</li>
      <li class="major"><span>6. Pricing</span>14</li><li><span>7. Terms &amp; Conditions</span>15</li>
    </ul>
    <div class="page-foot"><span>NovaLink Proposal</span><span>3</span></div>
  </div>
</section>

<section class="spread col-b row-2">
  <div class="page left">
    <div class="page-head"><div class="logo"><i></i>NOVALINK</div></div>
    <div class="page-head-rule"></div>
    <div class="title">Corporate Statement<small></small></div>
    <div class="body" style="top:70px;right:120px">
      <p>NovaLink is a privately owned systems integrator operating since 2006, with offices and technical staff across two regional sites.</p>
      <p>We have delivered sustained, profitable growth year on year through trusted partnerships.</p>
      <p>We hold advanced specialisations across network, security and collaboration.</p>
    </div>
    <div class="abs ph grey" style="right:18px;top:70px;width:95px;height:110px" role="img" aria-label="Portrait of the managing director"></div>
    <div class="abs" style="right:18px;top:184px;width:95px;font-size:4.8px;color:var(--navy);font-weight:600">Name Surname<br><span style="font-weight:400;color:var(--mute)">Managing Director</span></div>
    <div class="page-foot"><span>NovaLink Proposal</span><span>4</span></div>
  </div>
  <div class="page right">
    <div class="page-head"><div class="logo"><i></i>NOVALINK</div></div>
    <div class="page-head-rule"></div>
    <div class="title">Overview<small></small></div>
    <div class="abs ph" style="left:18px;right:18px;top:66px;height:95px" role="img" aria-label="Hand touching a glowing network interface"></div>
    <div class="body cols cols-2" style="top:172px">
      <div><div class="sub">Our Approach</div><p>We design, deliver and support secure network solutions for healthcare and enterprise clients.</p><p>Our engineers work alongside your team from planning to handover.</p></div>
      <div style="background:var(--navy);color:var(--white);padding:6px"><div class="sub" style="color:var(--white)">Key Facts</div><p>A leading provider in the regional healthcare sector.</p><p>Operating since 2006.</p></div>
    </div>
    <div class="page-foot"><span>NovaLink Proposal</span><span>5</span></div>
  </div>
</section>

<section class="spread col-a row-3">
  <div class="page left">
    <div class="page-head"><div class="logo"><i></i>NOVALINK</div></div>
    <div class="page-head-rule"></div>
    <div class="title">Executive Team<small></small></div>
    <div class="body cols cols-2" style="top:72px;row-gap:18px">
      <div><div class="ph grey circle" style="width:42px;height:42px;margin-bottom:4px" role="img" aria-label="Team member portrait"></div><div class="sub">Name Surname</div><p>Role title. Brief biography and key experience.</p></div>
      <div><div class="ph grey circle" style="width:42px;height:42px;margin-bottom:4px" role="img" aria-label="Team member portrait"></div><div class="sub">Name Surname</div><p>Role title. Brief biography and key experience.</p></div>
      <div><div class="ph grey circle" style="width:42px;height:42px;margin-bottom:4px" role="img" aria-label="Team member portrait"></div><div class="sub">Name Surname</div><p>Role title. Brief biography and key experience.</p></div>
      <div><div class="ph grey circle" style="width:42px;height:42px;margin-bottom:4px" role="img" aria-label="Team member portrait"></div><div class="sub">Name Surname</div><p>Role title. Brief biography and key experience.</p></div>
    </div>
    <div class="page-foot"><span>NovaLink Proposal</span><span>6</span></div>
  </div>
  <div class="page right">
    <div class="page-head"><div class="logo"><i></i>NOVALINK</div></div>
    <div class="page-head-rule"></div>
    <div class="title">Our Service<small></small></div>
    <div class="abs ph" style="left:18px;right:18px;top:66px;height:95px" role="img" aria-label="Team meeting in a bright office"></div>
    <div class="body cols cols-3" style="top:172px;text-align:center">
      <div><svg width="22" height="22"><circle cx="11" cy="11" r="10" fill="var(--blue)"/><path d="M6 11l3 3 7-7" stroke="#fff" stroke-width="1.6" fill="none"/></svg><div class="sub">Design</div><p>Tailored architecture for your needs.</p></div>
      <div><svg width="22" height="22"><circle cx="11" cy="11" r="10" fill="var(--blue)"/><path d="M6 11h10M12 7l4 4-4 4" stroke="#fff" stroke-width="1.6" fill="none"/></svg><div class="sub">Deliver</div><p>Certified engineers on every project.</p></div>
      <div><svg width="22" height="22"><circle cx="11" cy="11" r="10" fill="var(--blue)"/><path d="M7 9a4 4 0 018 0v3M7 12h8v3H7z" stroke="#fff" stroke-width="1.4" fill="none"/></svg><div class="sub">Support</div><p>Ongoing managed service options.</p></div>
    </div>
    <div class="body" style="top:250px"><p>We support the full lifecycle of your technology investment, from first workshop to long-term operation.</p></div>
    <div class="page-foot"><span>NovaLink Proposal</span><span>7</span></div>
  </div>
</section>

<section class="spread col-b row-3">
  <div class="page left">
    <div class="page-head"><div class="logo"><i></i>NOVALINK</div></div>
    <div class="page-head-rule"></div>
    <div class="title">2 Columns<small></small></div>
    <div class="abs ph" style="left:18px;right:18px;top:66px;height:110px" role="img" aria-label="Rows of server racks in a data centre"></div>
    <div class="body cols cols-2" style="top:186px">
      <div><div class="sub">Subheading</div><p>Two column body text for longer sections of the proposal.</p><p>Keep paragraphs short and focused on client outcomes.</p></div>
      <div><div class="sub">Subheading</div><p>Use this layout to compare options or present parallel topics.</p><p>Images span both columns above.</p></div>
    </div>
    <div class="page-foot"><span>NovaLink Proposal</span><span>8</span></div>
  </div>
  <div class="page right">
    <div class="page-head"><div class="logo"><i></i>NOVALINK</div></div>
    <div class="page-head-rule"></div>
    <div class="title">Heading Template<small></small></div>
    <div class="body" style="top:70px">
      <div class="sub">Heading Level 2</div>
      <p>Body copy sits here in a single column for standard proposal content and descriptive sections.</p>
      <p>Write clear statements about scope, approach and the value delivered to the client.</p>
      <div class="sub">Heading Level 3</div>
      <p>• Bullet point item one<br>• Bullet point item two<br>• Bullet point item three</p>
      <div class="sub">Heading Level 3</div>
      <p>Further supporting text describing deliverables, timelines and responsibilities for each party.</p>
      <p>Closing paragraph summarising the section.</p>
    </div>
    <div class="page-foot"><span>NovaLink Proposal</span><span>9</span></div>
  </div>
</section>

<section class="spread col-a row-4">
  <div class="page left">
    <div class="page-head"><div class="logo"><i></i>NOVALINK</div></div>
    <div class="page-head-rule"></div>
    <div class="title">Executive Team<small></small></div>
    <div class="body" style="top:72px">
      <div style="display:flex;gap:8px;margin-bottom:14px"><div class="ph grey circle" style="flex:none;width:42px;height:42px" role="img" aria-label="Team member portrait"></div><div><div class="sub">Name Surname</div><p>Role title. Brief biography and key experience.</p></div></div>
      <div style="display:flex;gap:8px;margin-bottom:14px"><div class="ph grey circle" style="flex:none;width:42px;height:42px" role="img" aria-label="Team member portrait"></div><div><div class="sub">Name Surname</div><p>Role title. Brief biography and key experience.</p></div></div>
      <div style="display:flex;gap:8px"><div class="ph grey circle" style="flex:none;width:42px;height:42px" role="img" aria-label="Team member portrait"></div><div><div class="sub">Name Surname</div><p>Role title. Brief biography and key experience.</p></div></div>
    </div>
    <div class="page-foot"><span>NovaLink Proposal</span><span>10</span></div>
  </div>
  <div class="page right">
    <div class="page-head"><div class="logo"><i></i>NOVALINK</div></div>
    <div class="page-head-rule"></div>
    <div class="title">Our Service<small></small></div>
    <div class="abs ph" style="left:18px;right:18px;top:66px;height:95px" role="img" aria-label="Colleagues collaborating at a desk"></div>
    <div class="body cols cols-3" style="top:172px">
      <div><div class="sub">Network</div><p>Enterprise campus and WAN design.</p></div>
      <div><div class="sub">Security</div><p>Firewall and threat protection.</p></div>
      <div><div class="sub">Collaboration</div><p>Voice, video and contact centre.</p></div>
    </div>
    <div class="page-foot"><span>NovaLink Proposal</span><span>11</span></div>
  </div>
</section>

<section class="spread col-b row-4">
  <div class="page left">
    <div class="page-head"><div class="logo"><i></i>NOVALINK</div></div>
    <div class="page-head-rule"></div>
    <div class="title">Operational Reporting<small></small></div>
    <svg class="abs" style="left:18px;top:64px" width="249" height="170" viewBox="0 0 249 170" font-family="Open Sans, sans-serif">
      <g stroke="var(--sky)" stroke-width="1"><line x1="124" y1="85" x2="50" y2="35"/><line x1="124" y1="85" x2="198" y2="35"/><line x1="124" y1="85" x2="50" y2="135"/><line x1="124" y1="85" x2="198" y2="135"/></g>
      <circle cx="124" cy="85" r="34" fill="var(--navy)"/>
      <text x="124" y="88" text-anchor="middle" font-family="Montserrat, sans-serif" font-size="7" font-weight="700" fill="#fff">REPORTING</text>
      <circle cx="50" cy="35" r="20" fill="var(--blue)"/><text x="50" y="37" text-anchor="middle" font-size="5" fill="#fff">Monitor</text>
      <circle cx="198" cy="35" r="20" fill="var(--sky)"/><text x="198" y="37" text-anchor="middle" font-size="5" fill="#fff">Analyse</text>
      <circle cx="50" cy="135" r="20" fill="var(--sky)"/><text x="50" y="137" text-anchor="middle" font-size="5" fill="#fff">Review</text>
      <circle cx="198" cy="135" r="20" fill="var(--blue)"/><text x="198" y="137" text-anchor="middle" font-size="5" fill="#fff">Improve</text>
    </svg>
    <svg class="abs" style="left:18px;top:248px" width="249" height="110" viewBox="0 0 249 110">
      <line x1="0" y1="100" x2="249" y2="100" stroke="var(--rule)"/>
      <g fill="var(--navy)"><rect x="10" y="50" width="12" height="50"/><rect x="50" y="30" width="12" height="70"/><rect x="90" y="60" width="12" height="40"/><rect x="130" y="20" width="12" height="80"/><rect x="170" y="40" width="12" height="60"/><rect x="210" y="10" width="12" height="90"/></g>
      <g fill="var(--sky)"><rect x="24" y="65" width="12" height="35"/><rect x="64" y="45" width="12" height="55"/><rect x="104" y="70" width="12" height="30"/><rect x="144" y="35" width="12" height="65"/><rect x="184" y="55" width="12" height="45"/><rect x="224" y="30" width="12" height="70"/></g>
    </svg>
    <div class="page-foot"><span>NovaLink Proposal</span><span>12</span></div>
  </div>
  <div class="page right">
    <div class="page-head"><div class="logo"><i></i>NOVALINK</div></div>
    <div class="page-head-rule"></div>
    <div class="title">Heading Template<small></small></div>
    <div class="body" style="top:70px">
      <p>Tables present pricing, service levels and scope items in a consistent style.</p>
      <table style="margin:6px 0 10px"><tr><th>Item</th><th>Description</th><th>Qty</th><th>Price</th></tr>
        <tr><td>01</td><td>Core switch</td><td>2</td><td>$0.00</td></tr><tr class="hl"><td>02</td><td>Access switch</td><td>12</td><td>$0.00</td></tr>
        <tr><td>03</td><td>Firewall</td><td>2</td><td>$0.00</td></tr><tr class="hl"><td>04</td><td>Wireless AP</td><td>40</td><td>$0.00</td></tr>
        <tr><td>05</td><td>Installation</td><td>1</td><td>$0.00</td></tr><tr class="hl"><td>06</td><td>Support</td><td>1</td><td>$0.00</td></tr>
        <tr><td colspan="3"><b>Total</b></td><td><b>$0.00</b></td></tr></table>
      <div class="sub">Notes</div>
      <p>• Prices exclude GST<br>• Valid for 30 days<br>• Subject to terms</p>
    </div>
    <div class="page-foot"><span>NovaLink Proposal</span><span>13</span></div>
  </div>
</section>

<section class="spread col-a row-5">
  <div class="page left">
    <div class="page-head"><div class="logo"><i></i>NOVALINK</div></div>
    <div class="page-head-rule"></div>
    <div class="title">Sections<small></small></div>
    <div class="abs" style="left:70px;top:70px;width:70px;bottom:40px;background:var(--navy)"></div>
    <div class="body" style="top:78px">
      <div style="display:grid;grid-template-columns:46px 70px 1fr;row-gap:22px;column-gap:6px">
        <b style="color:var(--navy)">Phase 1</b><span style="color:#fff;padding-left:4px">Discovery</span><span>Workshops and requirements.</span>
        <b style="color:var(--navy)">Phase 2</b><span style="color:#fff;padding-left:4px">Design</span><span>High and low level design.</span>
        <b style="color:var(--navy)">Phase 3</b><span style="color:#fff;padding-left:4px">Build</span><span>Staging and configuration.</span>
        <b style="color:var(--navy)">Phase 4</b><span style="color:#fff;padding-left:4px">Deploy</span><span>Installation and cutover.</span>
        <b style="color:var(--navy)">Phase 5</b><span style="color:#fff;padding-left:4px">Support</span><span>Handover and ongoing care.</span>
      </div>
    </div>
    <div class="page-foot"><span>NovaLink Proposal</span><span>14</span></div>
  </div>
  <div class="page right">
    <div class="page-head"><div class="logo"><i></i>NOVALINK</div></div>
    <div class="page-head-rule"></div>
    <div class="title">Our Service<small></small></div>
    <div class="body" style="top:70px">
      <p>We work with a well established group of technology vendors to deliver complete solutions for every client.</p>
      <div class="sub">Specialisations</div>
      <p>✓ Advanced Enterprise Network Architecture<br>✓ Advanced Security Architecture<br>✓ Advanced Collaboration Architecture<br>✓ Advanced Unified Computing Technology<br>✓ Advanced Data Centre Architecture (in progress)</p>
      <div class="sub">Healthcare</div>
      <p>A leading provider of network products and services in the regional healthcare sector.</p>
      <div class="sub">Partner Status</div>
      <p>Gold partner status expected 2H2018.</p>
    </div>
    <div class="page-foot"><span>NovaLink Proposal</span><span>15</span></div>
  </div>
</section>

<section class="spread col-b row-5">
  <div class="page left">
    <div class="page-head"><div class="logo"><i></i>NOVALINK</div></div>
    <div class="page-head-rule"></div>
    <div class="title">Options<small></small></div>
    <div class="abs ph" style="left:18px;width:120px;top:66px;height:80px" role="img" aria-label="Video conference room"></div>
    <div class="body" style="top:70px;left:146px"><div class="sub">Option A</div><p>Standard deployment with core services included.</p></div>
    <div class="abs ph light" style="left:18px;width:120px;top:158px;height:80px" role="img" aria-label="Engineer working on a laptop"></div>
    <div class="body" style="top:162px;left:146px"><div class="sub">Option B</div><p>Extended deployment with managed services.</p></div>
    <div class="abs ph" style="left:18px;width:120px;top:250px;height:80px" role="img" aria-label="City skyline at dusk"></div>
    <div class="body" style="top:254px;left:146px"><div class="sub">Option C</div><p>Full lifecycle partnership and support.</p></div>
    <div class="page-foot"><span>NovaLink Proposal</span><span>16</span></div>
  </div>
  <div class="page right">
    <div class="page-head"><div class="logo"><i></i>NOVALINK</div></div>
    <div class="page-head-rule"></div>
    <div class="title">Structure Chart<small></small></div>
    <svg class="abs" style="left:18px;top:70px" width="249" height="230" viewBox="0 0 249 230" font-family="Montserrat, sans-serif" font-size="5" text-anchor="middle">
      <g stroke="var(--mute)" fill="none"><path d="M124 30V50M40 50H208M40 50V70M124 50V70M208 50V70M124 100V130M80 130H168M80 130V150M168 130V150M168 180V200"/></g>
      <rect x="84" y="8" width="80" height="22" fill="var(--navy)"/><text x="124" y="22" fill="#fff">Executive Sponsor</text>
      <rect x="4" y="70" width="72" height="30" fill="var(--pale)" stroke="var(--navy)"/><text x="40" y="88" fill="var(--navy)">Account Manager</text>
      <rect x="88" y="70" width="72" height="30" fill="var(--blue)"/><text x="124" y="88" fill="#fff">Project Manager</text>
      <rect x="172" y="70" width="72" height="30" fill="var(--pale)" stroke="var(--navy)"/><text x="208" y="88" fill="var(--navy)">Service Manager</text>
      <rect x="44" y="150" width="72" height="30" fill="var(--pale)" stroke="var(--navy)"/><text x="80" y="168" fill="var(--navy)">Lead Engineer</text>
      <rect x="132" y="150" width="72" height="30" fill="var(--pale)" stroke="var(--navy)"/><text x="168" y="168" fill="var(--navy)">Security Engineer</text>
      <rect x="132" y="200" width="72" height="26" fill="var(--sky)"/><text x="168" y="216" fill="#fff">Field Technicians</text>
    </svg>
    <div class="page-foot"><span>NovaLink Proposal</span><span>17</span></div>
  </div>
</section>

</body>
</html>
```